Brindle Gateworks garage door installation service and repairs

I need a business card design for my company that is called Brindle Gateworks, I install, service, repair and automate garaged doors.
I want my card to look simple and neat but I also want the information such as contact number, email address and website to be clear and noticeable. I would love a simple logo if possible, I would like to see the color blue in the card but not overpowering.

Industry/Entity Type

Garage

```html
<!DOCTYPE html>
<html lang="en">
<head>
<meta charset="utf-8">
<title>Brindle Gateworks – Business Card</title>
<link href="https://fonts.googleapis.com/css2?family=Montserrat:wght@300;400;500;700&display=swap" rel="stylesheet">
<style>
  :root {
    --page: #ffffff;
    --card: #f5f5f5;
    --card-edge: #c9c9c9;
    --ink-dark: #333333;
    --ink-mid: #555555;
    --brand-blue: #2a6fba;
  }
  * { margin: 0; padding: 0; box-sizing: border-box; }
  html, body {
    width: 1200px; height: 662px; overflow: hidden;
    background: var(--page);
    font-family: "Montserrat", sans-serif;
  }
  .canvas { position: relative; width: 1200px; height: 662px; }
  .card {
    position: absolute; left: 188px; top: 2px; width: 1007px; height: 652px;
    border: 4px solid var(--card-edge);
    background: linear-gradient(135deg, #f8f8f8 0%, var(--card) 60%, #f1f1f1 100%);
  }
  .card-divider {
    position: absolute; left: 372px; top: 190px; width: 24px; height: 280px;
    background: linear-gradient(90deg, rgba(0,0,0,0) 0%, rgba(0,0,0,0.035) 50%, rgba(0,0,0,0) 100%);
  }
  .identity {
    position: absolute; right: 668px; top: 274px; text-align: right;
  }
  .identity-name {
    font-weight: 700; font-size: 30px; color: var(--ink-dark);
    letter-spacing: -0.2px; line-height: 38px;
  }
  .identity-title {
    font-weight: 300; font-size: 24px; color: var(--brand-blue); line-height: 34px;
  }
  .contact-list {
    position: absolute; left: 400px; top: 254px; list-style: none;
  }
  .contact-item {
    display: flex; align-items: center; height: 43.5px;
    font-weight: 400; font-size: 27px; color: var(--ink-mid);
  }
  .contact-icon { width: 34px; height: 34px; margin-right: 28px; flex: none; }
  .contact-icon path, .contact-icon rect { fill: var(--brand-blue); }
  .brand-lockup {
    position: absolute; right: 58px; top: 518px;
    display: flex; align-items: center; gap: 14px;
  }
  .brand-dot {
    width: 18px; height: 18px; border-radius: 50%; background: var(--brand-blue);
  }
  .brand-name {
    font-weight: 500; font-size: 40px; color: var(--ink-mid); letter-spacing: -0.5px;
  }
</style>
</head>
<body>
<main class="canvas">
  <section class="card">
    <div class="card-divider"></div>

    <div class="identity">
      <p class="identity-name">Name of person</p>
      <p class="identity-title">Title of Position</p>
    </div>

    <ul class="contact-list">
      <li class="contact-item">
        <svg class="contact-icon" viewBox="0 0 34 34" aria-hidden="true">
          <path d="M3 12c0-4 6-6 14-6s14 2 14 6v2h-7v-3c-2-1-12-1-14 0v3H3z"/>
          <path d="M9 15h16l3 9H6z"/>
          <rect x="15" y="17" width="4" height="4" rx="2" style="fill:#f5f5f5"/>
        </svg>
        <span>+44 (0)7700 900417</span>
      </li>
      <li class="contact-item">
        <svg class="contact-icon" viewBox="0 0 34 34" aria-hidden="true">
          <rect x="2" y="9" width="30" height="18" rx="1"/>
          <path d="M2 10l15 10 15-10" style="fill:none;stroke:#f5f5f5;stroke-width:1.6"/>
        </svg>
        <span>hello@brindlegateworks.com</span>
      </li>
      <li class="contact-item">
        <svg class="contact-icon" viewBox="0 0 34 34" aria-hidden="true">
          <path d="M4 4l17 6-5 3 12 12-3 3-12-12-3 5z"/>
        </svg>
        <span>www.brindlegateworks.com</span>
      </li>
    </ul>

    <div class="brand-lockup">
      <span class="brand-dot"></span>
      <span class="brand-name">Brindle Gateworks</span>
    </div>
  </section>
</main>
</body>
</html>
```